Electrical contractor

looking for a standard sized, horizontal, double sided business card for an electrical contractors business.
i have played around on microsoft word (only computer program i know how to use!) and will attach what i have made so far, really open to any ideas. i just want the ROFT to stand out to the rest of the business name.

i wish to use the colours black and green, and white for writing. i will attach the pictures i took off google, i want to either use them, or somethin similar for the back grounds

i wish the front to have the following info:
business name: R.O.F.T ELECTRICAL CONTRACTORS
MY NAME; DARREN HOLT
STATUS; A CLASS ELECTRICIAN
LICENSE NO; TRK784150
PH NO. 0437615942
EMAIL ADD. ROFT.ELECTRICAL@VOLTMAILBOX.COM
AND MY SLOGAN: where excellence meets integrity, and service comes with a smile.

i am not sure what to have on the back, other than what i do for work.eg titled WHAT WE DO
i dont want too much written on there or will look crowded, but options to add to back, from most important to least, please pick however many you think will look the best
new homes/extentions
led lighting and downlights
Solar Power
power
safety switches
switchboards
telephone and tv
smoke alarms
stoves and ovens
hot water systems
fault finding
re wiring
Updates

Thank you to those who have submitted designs, I would like to change my slogan to something more simple, I'm thinking something like. RELIABLE. EFFICIENT. PROFESSIONAL. AFFORDABLE. in what ever order you thinks fits best. Thanks

```html
<!DOCTYPE html>
<html lang="en">
<head>
<meta charset="utf-8">
<title>R.O.F.T Electrical Contractors – Business Card</title>
<link rel="stylesheet" href="https://fonts.googleapis.com/css2?family=Dosis:wght@300;400;500;600;700&family=Yanone+Kaffeesatz:wght@400&display=swap">
<style>
  :root {
    --black: #000000;
    --white: #ffffff;
    --green: #0c8a0c;
    --green-bright: #3fe03a;
    --green-glow: #7dff5a;
    --band-top: #2fae2a;
    --band-bottom: #0a6a0a;
    --logo-text: #8cf06e;
  }
  * { margin: 0; padding: 0; box-sizing: border-box; }
  html, body {
    width: 981px; height: 1200px; overflow: hidden; background: var(--black);
  }
  .card {
    position: relative; width: 981px; height: 1200px; background: var(--black);
    font-family: "Dosis", sans-serif; color: var(--white);
  }
  .front {
    position: absolute; left: 0; top: 0; width: 981px; height: 522px;
    background: var(--black); overflow: hidden;
  }
  .bulb-photo {
    position: absolute; right: 0; top: 0; width: 360px; height: 522px;
    background:
      radial-gradient(ellipse 110px 170px at 300px 250px, #c8ff9a 0%, #4ee03a 30%, #118a10 60%, rgba(0,40,0,0) 100%),
      radial-gradient(ellipse 320px 360px at 300px 220px, rgba(40,160,30,.55) 0%, rgba(0,0,0,0) 75%);
  }
  .brand-title {
    position: absolute; left: 62px; top: 52px;
    font-weight: 300; font-size: 88px; line-height: 1; letter-spacing: 2px;
  }
  .brand-sub {
    position: absolute; left: 63px; top: 138px;
    font-weight: 400; font-size: 24px; letter-spacing: 0.5px;
  }
  .contact { position: absolute; left: 63px; top: 326px; }
  .contact-name { font-weight: 600; font-size: 34px; letter-spacing: 1px; line-height: 1; margin-bottom: 8px; }
  .contact-line { font-weight: 400; font-size: 26px; line-height: 32px; letter-spacing: 0.5px; }
  .slogan-band {
    position: absolute; left: 0; top: 523px; width: 981px; height: 77px;
    background: linear-gradient(var(--band-top), var(--band-bottom));
    border-top: 2px solid #52c84a;
  }
  .slogan {
    position: absolute; left: 0; top: 13px; width: 981px; text-align: center;
    font-weight: 600; font-size: 21px; letter-spacing: 1px; font-variant: small-caps;
  }
  .back-logo-area {
    position: absolute; left: 0; top: 600px; width: 593px; height: 600px; background: var(--black);
    overflow: hidden;
  }
  .lightning-art {
    position: absolute; inset: 0;
    background: radial-gradient(ellipse 280px 240px at 285px 330px, rgba(60,200,40,.45) 0%, rgba(20,90,10,.2) 55%, rgba(0,0,0,0) 100%);
  }
  .logo-name {
    position: absolute; left: 0; top: 298px; width: 593px; text-align: center;
    font-weight: 500; font-size: 26px; letter-spacing: 1px; color: var(--logo-text);
  }
  .services {
    position: absolute; left: 593px; top: 600px; width: 388px; height: 600px;
    background: var(--green); list-style: none; padding-top: 30px;
  }
  .services li {
    font-family: "Yanone Kaffeesatz", sans-serif; font-size: 30px; letter-spacing: 1px;
    text-align: center; height: 46.2px; line-height: 46px; color: var(--white);
  }
</style>
</head>
<body>
<div class="card">
  <section class="front">
    <div class="bulb-photo" role="img" aria-label="Glowing green light bulb photograph"></div>
    <div class="brand-title">R.O.F.T</div>
    <div class="brand-sub">ELECTRICAL CONTRACTORS</div>
    <div class="contact">
      <div class="contact-name">DARREN HOLT</div>
      <div class="contact-line">A CLASS ELECTRICIAN</div>
      <div class="contact-line">LICENSE NO ; TRK784150</div>
      <div class="contact-line">PH NO. : 0437615942</div>
      <div class="contact-line">EMAIL : ROFT.ELECTRICAL@VOLTMAILBOX.COM</div>
    </div>
  </section>

  <div class="slogan-band">
    <p class="slogan">Where excellence meets integrity, and service comes with a smile.</p>
  </div>

  <section class="back-logo-area">
    <div class="lightning-art" role="img" aria-label="Green electric lightning glow on black background"></div>
    <div class="logo-name">R.O.F.T ELECTRICAL CONTRACTORS</div>
  </section>

  <ul class="services">
    <li>NEW HOMES/EXTENTIONS</li>
    <li>LED LIGHTING AND DOWNLIGHTS</li>
    <li>SOLAR POWER</li>
    <li>POWER</li>
    <li>SAFETY SWITCHES</li>
    <li>SWITCHBOARDS</li>
    <li>TELEPHONE AND TV</li>
    <li>SMOKE ALARMS</li>
    <li>STOVES AND OVENS</li>
    <li>HOT WATER SYSTEMS</li>
    <li>FAULT FINDING</li>
    <li>RE WIRING</li>
  </ul>
</div>
</body>
</html>
```